PROMOTION CARD for NEW APPLICATION LAUNCH

Hi need double sided promotion card the size of a postcard.
we car launching a new app, and need to promote
the app is focused on the automotive
the functions are to help remind customers when there car utilities bills are due.
* registration
*Insurance
*CTP due
*Service
* Warranty

Helps sell your car under the ( "Whats New " Button )
Helps you find a better finance or insurance deal.( Zenqa Portal)

Target Market(s)

All consumers who own a Car all ages both male and female

Industry/Entity Type

Automotive

Font styles to use
Sans Serif

Colors
0293ce
9ccb3b
fffbf0

Requirements
Must have
• clean and professional makes you want to down load the app
Nice to have
• clear description about what the app dose feature and functions
• the application will reminder the customer when the
• *registration due
• * insurance due
• *Finance due
• Kelvra picture
• car or road in background
• *CTP due
• *Service due
• *Warranty Due
• it will also pay a payment function so you can pay,
Should not have
• color brown/ no running writing

```html
<!DOCTYPE html>
<html lang="en">
<head>
<meta charset="utf-8">
<title>Drivora – Promotion Card</title>
<link rel="stylesheet" href="https://fonts.googleapis.com/css2?family=Open+Sans:ital,wght@0,700;0,800;1,700;1,800&family=Lato:ital,wght@0,400;0,700;1,400&display=swap">
<style>
  :root {
    --blue: #0293ce;
    --blue-deep: #0c5ea8;
    --green: #9ccb3b;
    --green-deep: #6fa51e;
    --cream: #fffbf0;
    --ink: #1b1b1b;
    --text: #2a2a2a;
    --silver-light: #ffffff;
    --silver-mid: #e4e4e4;
    --silver-dark: #a9a9a9;
    --stage: #ecebe7;
  }
  * { box-sizing: border-box; margin: 0; padding: 0; }
  html, body { width: 900px; height: 1200px; overflow: hidden; }
  body {
    background: var(--stage);
    position: relative;
    font-family: "Lato", sans-serif;
    color: var(--text);
  }
  .card {
    position: absolute;
    width: 660px;
    height: 505px;
    left: 120px;
    overflow: hidden;
    background: linear-gradient(180deg, var(--silver-light) 0%, #f3f3f3 55%, var(--silver-mid) 100%);
    box-shadow: 0 6px 18px rgba(0,0,0,.18);
  }
  .card--front { top: 55px; }
  .card--back { top: 640px; }
  .card__art { position: absolute; inset: 0; }
  .abs { position: absolute; }

  /* brand mark */
  .brand { position: absolute; display: flex; flex-direction: column; align-items: flex-start; gap: 6px; }
  .brand__square { width: 58px; height: 58px; background: var(--blue); }
  .brand__name { font-family: "Lato", sans-serif; font-weight: 700; font-size: 22px; color: var(--ink); line-height: 1; }

  /* headlines */
  .headline { display: block; font-family: "Open Sans", sans-serif; font-style: italic; font-weight: 800; line-height: 1; letter-spacing: -0.5px; }
  .headline--blue { color: var(--blue-deep); }
  .headline--green { color: var(--green-deep); }
  .rule { position: absolute; height: 4px; background: var(--ink); }

  /* tabs */
  .tab {
    position: absolute; height: 28px; color: #fff;
    font-family: "Open Sans", sans-serif; font-weight: 700;
    display: flex; align-items: center;
    background: linear-gradient(180deg, #b3dc57, var(--green-deep));
  }
  .tab--left { left: 0; padding-left: 28px; font-size: 18px; clip-path: polygon(0 0, 100% 0, 92% 100%, 0 100%); }
  .tab--right { right: 0; padding-left: 22px; font-size: 13px; clip-path: polygon(6% 0, 100% 0, 100% 100%, 0 100%); }

  /* front body */
  .lead { font-style: italic; font-size: 15.5px; line-height: 1.3; color: var(--ink); }
  .checklist { list-style: none; display: grid; grid-template-columns: 158px 130px; row-gap: 5px; font-style: italic; font-size: 15.5px; color: var(--ink); }
  .checklist li { display: flex; align-items: center; gap: 9px; }
  .checklist li::before { content: ""; width: 9px; height: 9px; background: var(--green); flex: none; }
  .band-copy { font-weight: 700; font-size: 18.5px; line-height: 1.3; color: var(--ink); }
  .band-copy p + p { margin-top: 8px; }

  /* back body */
  .intro { font-size: 14px; line-height: 1.35; text-align: right; color: var(--ink); }
  .features { list-style: none; text-align: right; font-size: 12px; line-height: 1.35; color: var(--ink); }
  .features li { display: flex; justify-content: flex-end; align-items: flex-start; gap: 6px; margin-bottom: 4px; }
  .features li::after { content: ""; width: 8px; height: 8px; margin-top: 4px; background: var(--green); flex: none; }
  .features li span { max-width: 300px; }
  .social { position: absolute; display: flex; gap: 16px; align-items: center; }
  .social__tile { width: 34px; height: 34px; }
  .social__tile--blue { background: #2b9fd9; }
  .social__tile--navy { background: #3b5a9a; }
  .social__tile--tan { background: #b79a7a; }
</style>
</head>
<body>

<!-- FRONT -->
<section class="card card--front">
  <svg class="card__art" width="660" height="505" viewBox="0 0 660 505">
    <defs>
      <linearGradient id="blueArc" x1="0" y1="0" x2="1" y2="1">
        <stop offset="0" stop-color="#1a8fd6"/><stop offset="1" stop-color="#0b4f9c"/>
      </linearGradient>
      <linearGradient id="greenBand" x1="0" y1="0" x2="0" y2="1">
        <stop offset="0" stop-color="#b6dd5a"/><stop offset="1" stop-color="#7cb027"/>
      </linearGradient>
      <linearGradient id="silverArc" x1="0" y1="0" x2="1" y2="0">
        <stop offset="0" stop-color="#cfcfcf"/><stop offset=".5" stop-color="#ffffff"/><stop offset="1" stop-color="#9a9a9a"/>
      </linearGradient>
    </defs>
    <path d="M0 0 H660 V14 C560 6 480 14 400 26 H0 Z" fill="url(#blueArc)"/>
    <path d="M660 20 C520 50 420 150 410 300 C405 400 450 470 520 505 H660 Z" fill="url(#blueArc)"/>
    <path d="M395 505 C330 430 325 300 380 200 C420 130 500 70 560 50 C480 110 430 200 425 300 C420 400 450 470 480 505 Z" fill="url(#silverArc)"/>
    <path d="M0 365 H355 C340 400 345 450 365 485 H0 Z" fill="url(#greenBand)"/>
    <rect x="0" y="485" width="400" height="20" fill="#ffffff"/>
  </svg>

  <div class="brand" style="left:30px;top:18px;">
    <span class="brand__square"></span>
    <span class="brand__name">drivora</span>
  </div>
  <h1 class="abs" style="left:120px;top:24px;">
    <span class="headline headline--blue" style="font-size:40px;">WE REMEMBER</span>
    <span class="headline headline--green" style="font-size:33px;margin-top:2px;">WHAT YOU FORGET!</span>
  </h1>
  <div class="rule" style="left:25px;top:112px;width:580px;"></div>

  <div class="tab tab--left" style="top:127px;width:132px;">Functions</div>
  <p class="lead abs" style="left:25px;top:165px;width:205px;">The application will reminder the customer when the</p>
  <ul class="checklist abs" style="left:30px;top:212px;">
    <li>Registratiton due</li><li>CTP due</li>
    <li>Insurance due</li><li>Service due</li>
    <li>Finance due</li><li>Warranty Due</li>
  </ul>
  <p class="lead abs" style="left:25px;top:295px;width:235px;">It will also pay a payment function so you can pay.</p>

  <div class="band-copy abs" style="left:30px;top:378px;width:300px;">
    <p>Helps sell your car under the<br>( "Whats New " Button )</p>
    <p>Helps you find a better finance or insurance deal.( Zenqa Portal)</p>
  </div>

  <div class="abs" role="img" aria-label="Hand holding a Kelvra smartphone showing the app home screen with round function icons and a car photo"
       style="left:385px;top:118px;width:215px;height:387px;border-radius:26px 26px 0 0;background:linear-gradient(160deg,#2b2f36 0%,#3b5f8a 45%,#e5b9a0 80%,#f0c8ae 100%);"></div>
</section>

<!-- BACK -->
<section class="card card--back">
  <svg class="card__art" width="660" height="505" viewBox="0 0 660 505">
    <defs>
      <linearGradient id="blueTop" x1="0" y1="0" x2="1" y2="0">
        <stop offset="0" stop-color="#1a8fd6"/><stop offset="1" stop-color="#0b4f9c"/>
      </linearGradient>
      <linearGradient id="greenFoot" x1="0" y1="0" x2="0" y2="1">
        <stop offset="0" stop-color="#b6dd5a"/><stop offset="1" stop-color="#7cb027"/>
      </linearGradient>
      <linearGradient id="silverRim" x1="0" y1="0" x2="1" y2="0">
        <stop offset="0" stop-color="#9a9a9a"/><stop offset=".5" stop-color="#ffffff"/><stop offset="1" stop-color="#bdbdbd"/>
      </linearGradient>
    </defs>
    <path d="M0 0 H660 V10 C560 4 480 10 360 16 H0 Z" fill="url(#blueTop)"/>
    <rect x="330" y="422" width="330" height="63" fill="url(#greenFoot)"/>
    <rect x="0" y="485" width="660" height="20" fill="#ffffff"/>
    <path d="M0 245 H340 C385 300 395 420 360 505 H348 C378 420 370 305 325 255 H0 Z" fill="url(#silverRim)"/>
  </svg>

  <h1 class="abs" style="left:88px;top:14px;">
    <span class="headline headline--blue" style="font-size:56px;font-style:normal;letter-spacing:1px;">DRIVORA</span>
    <span class="headline headline--green" style="font-size:42px;margin-top:2px;">FREE DOWNLOAD</span>
  </h1>
  <div class="brand" style="left:495px;top:24px;">
    <span class="brand__square"></span>
    <span class="brand__name">drivora</span>
  </div>
  <div class="rule" style="left:25px;top:121px;width:600px;"></div>

  <div class="tab tab--right" style="top:135px;width:168px;">DRIVORA FEATURES</div>
  <p class="intro abs" style="left:50px;top:170px;width:582px;">Lorem Ipsum is simply dummy text of the printing and typesetting industry. Lorem Ipsum has been the industry's standard dummy text ever since the 1500s, when an unknown printer took a galley of type and scrambled it to make a type specimen book.</p>
  <div class="tab tab--right" style="top:233px;width:168px;">SPECIAL FEATURES</div>

  <div class="abs" role="img" aria-label="Happy woman with raised arms leaning out of a white car window under a bright sky"
       style="left:0;top:255px;width:338px;height:250px;border-radius:0 140px 0 0;background:linear-gradient(180deg,#9cc2e2 0%,#cfe0ec 45%,#6f8f5a 70%,#d9dcdf 100%);"></div>

  <ul class="features abs" style="right:22px;top:278px;width:330px;">
    <li><span>Lorem ipsum dolor sit amet, consectetur adipiscing elit.</span></li>
    <li><span>Nullam non dolor eu eros porta maximus ac ac augue.</span></li>
    <li><span>Vestibulum semper lectus eget hendrerit aliquam</span></li>
    <li><span>Ut ut diam aliquet, sodales nisi mollis</span></li>
    <li><span>Etiam lacinia tortor non convallis viverra.</span></li>
    <li><span style="max-width:200px;">Nulla id nisl condimentum, molestie risus vel,condimentum mauris.</span></li>
  </ul>

  <div class="social" style="left:400px;top:437px;">
    <span class="social__tile social__tile--blue"></span>
    <svg width="40" height="34" viewBox="0 0 40 34" aria-label="Email">
      <rect x="2" y="5" width="36" height="24" fill="#1f6fb5"/>
      <path d="M2 5 L20 19 L38 5" fill="none" stroke="#fff" stroke-width="2"/>
    </svg>
    <svg width="26" height="36" viewBox="0 0 26 36" aria-label="Location">
      <path d="M13 1 C6 1 1 6 1 13 C1 22 13 35 13 35 C13 35 25 22 25 13 C25 6 20 1 13 1 Z" fill="#1f6fb5"/>
      <circle cx="13" cy="13" r="4.5" fill="#fff"/>
    </svg>
    <span class="social__tile social__tile--tan"></span>
    <span class="social__tile social__tile--navy"></span>
  </div>
</section>

</body>
</html>
```